Label designs for three different cider varieties

The Hollin Perry Works is a family run business. We have been making cider within the family as a hobby for over 100 years and we have recently decided to start to try to sell the cider. Therefore this project is to create a logo and three product labels for three different varieties of cider. So we should end up with four files; one for the logo and one for each of the labels. The files need to be in an editable format for us so that we can add edit the batch numbers e.g. PNG file.
For the logo we would like to use the Lark Family Shield since Lark is our family name. We would like it adapted into a cider themed crest, for example with apples and trees. We are open to ideas about the logo but this is just our initial idea. Example of the original Lark Family Shield can be seen in the link below:
http://www.plumevault.net/coats/Lark-England.jpg
The labels should be no bigger than 93mm in height and 213mm in length. Each label should be similar in style so it is clear the three different varieties of cider are from the same company. Each label must have the following information since this is a legal requirement:
- The logo you have created
- The Hollin Perry Works Ltd.
- 42 Milford Terrace, Taunton, Somerset, TA4 9QJ
- Alcohol: 6% vol
- 500ml
- Allergens: Contains Sulphites for freshness
- There needs to be space on the label for batch numbers. This is four numbers e.g. 1701.
- Family craft cider makers using only premium apples from our own traditional Somerset orchard.
The names of the three cider varieties are:
- Hollin Traditional
- Hollin Golden
- Hollin Quarrow
Our initial idea is that each variety would have its own colour associated with it; i.e. black themed label for Hollin Traditional, gold themed label for Hollin Golden and a red themed label for Hollin Quarrow. The crest logo you have created would then be in the themed colour for that cider variety i.e. black, gold or red.
We would like the labels to reflect the following themes for our brand:
- High end premium brand
- Clean and simple design
- Modern
Overall we are very open to ideas and we do not want to constrain your creativity. All of the above is just our initial ideas but we would love to see what ideas you have. The only things that cannot change are what must be on the label since this is a legal requirement we have to meet.

```html
<!DOCTYPE html>
<html lang="en">
<head>
<meta charset="utf-8">
<title>The Hollin Perry Works – Cyder Labels</title>
<link rel="stylesheet" href="https://fonts.googleapis.com/css2?family=Bebas+Neue&family=Oswald:wght@300;400;500;700&family=Playfair+Display:ital,wght@1,700&display=swap">
<style>
:root{
  --page:#ffffff;
  --gold:#d4ad4a;
  --gold-light:#f0d98a;
  --gold-dark:#9c7a28;
  --silver:#d9d9d9;
  --silver-dim:#b8b8b8;
  --black-top:#3a3a3a;
  --black-bottom:#1c1c1c;
  --red-top:#8a1a1e;
  --red-bottom:#5e0d10;
  --olive-top:#6a5524;
  --olive-bottom:#463611;
  --caption:#222222;
}
*{box-sizing:border-box;margin:0;padding:0}
html,body{width:754px;height:1200px;overflow:hidden;background:var(--page)}
body{position:relative;font-family:"Oswald",sans-serif;color:var(--silver)}

.frame{position:absolute;border:3px solid var(--gold);box-shadow:inset 0 0 0 1px var(--gold-dark)}

.banner{left:186px;top:38px;width:380px;height:95px;
  background:linear-gradient(var(--black-top),var(--black-bottom));
  border-left:none;border-right:none;display:flex;align-items:center;justify-content:center}

.brand-mark{display:flex;flex-direction:column;align-items:center;gap:3px;color:var(--gold);font-family:"Oswald",sans-serif;font-weight:500;text-transform:uppercase;text-align:center;line-height:1.05}
.brand-mark .dot{width:14px;height:14px;border-radius:50%;background:var(--gold)}
.banner .brand-mark{font-size:13px;width:90px}

.label{width:287px;height:309px;overflow:hidden}
.label.traditional{background:linear-gradient(var(--black-top),var(--black-bottom))}
.label.quarrow{background:linear-gradient(var(--red-top),var(--red-bottom))}
.label.golden{background:linear-gradient(var(--olive-top),var(--olive-bottom))}
.col-front{left:83px}
.col-back{left:387px}
.row-1{top:154px}
.row-2{top:494px}
.row-3{top:828px}

.label > *{position:absolute}

.fruit-art{border-radius:50%;background:radial-gradient(circle at 50% 50%,rgba(255,255,255,.10),rgba(255,255,255,.03) 65%,transparent 72%)}
.quarrow .fruit-art{background:radial-gradient(circle at 50% 50%,rgba(230,60,60,.30),rgba(230,60,60,.08) 65%,transparent 72%)}
.front .fruit-art{left:40px;top:40px;width:210px;height:210px}
.back .fruit-art{left:70px;top:110px;width:150px;height:150px}

.front .brand-mark{left:91px;top:10px;width:100px;font-size:14px}

.variety{left:0;width:100%;text-align:center;font-family:"Bebas Neue",sans-serif;color:var(--silver);line-height:.9;letter-spacing:.5px;text-shadow:0 1px 0 rgba(0,0,0,.5)}
.front .variety{top:118px;font-size:44px}
.style-line{left:0;width:100%;top:205px;text-align:center;font-family:"Playfair Display",serif;font-style:italic;font-weight:700;font-size:14px;color:var(--gold)}

.rule{height:0;border-top:1px dashed var(--gold)}
.front .rule.top{left:44px;right:44px;top:229px}
.front .rule.bottom{left:44px;right:44px;top:296px}

.facts{display:flex;align-items:stretch;color:var(--silver);text-transform:uppercase}
.front .facts{left:44px;right:44px;top:236px;height:55px}
.facts .measures{width:55px;display:flex;flex-direction:column;justify-content:space-between;align-items:center;font-size:9px;font-weight:500;line-height:1.2;text-align:center;padding:4px 0}
.facts .measures .vol{border-bottom:1px dashed var(--silver-dim);padding-bottom:4px}
.facts .claim{flex:1;border-left:1px solid var(--gold);border-right:1px solid var(--gold);font-size:8.3px;font-weight:300;line-height:1.38;text-align:center;padding:0 4px;display:flex;align-items:center}
.facts .tree{width:48px;display:flex;align-items:center;justify-content:center}
.tree-art{width:26px;height:42px;background:linear-gradient(var(--silver),var(--silver-dim));border-radius:45% 45% 6px 6px;opacity:.8}

.back .variety{left:36px;top:28px;width:auto;text-align:left;font-size:27px;line-height:.95}
.back .company{left:36px;top:82px;font-size:6.3px;font-weight:500;line-height:1.45;text-transform:uppercase;color:var(--silver)}
.back .brand-mark{left:186px;top:22px;width:72px;font-size:10px}
.back .rule.top{left:36px;right:36px;top:105px}
.back .facts{left:36px;right:36px;top:110px;height:62px}
.back .facts .claim{flex:0 0 104px;font-size:8px}
.back .facts .tree{flex-direction:column;justify-content:flex-end;width:auto;flex:1;padding-bottom:2px;gap:8px}
.back .tree-art{width:22px;height:34px}
.batch{font-size:6px;font-weight:500;white-space:nowrap}
.back .rule.mid{left:36px;right:36px;top:176px}
.allergens{left:0;width:100%;top:184px;text-align:center;font-size:8.5px;font-weight:500;text-transform:uppercase;color:var(--silver)}
.description{left:32px;right:30px;top:204px;font-size:7.4px;font-weight:300;line-height:1.3;color:var(--silver)}
.description p + p{margin-top:6px;font-size:6.6px}
.flourish{left:128px;top:293px;width:32px;height:4px;background:var(--gold);border-radius:2px;opacity:.8}

.size-caption{position:absolute;top:1152px;width:287px;text-align:center;font-family:"Oswald",sans-serif;font-weight:500;font-size:17px;color:var(--caption)}
</style>
</head>
<body>

<header class="frame banner">
  <div class="brand-mark"><span class="dot"></span><span>The Hollin Perry Works</span></div>
</header>

<!-- Hollin Traditional -->
<section class="frame label front traditional col-front row-1">
  <div class="fruit-art" role="img" aria-label="Engraved apple and leaf illustration"></div>
  <div class="brand-mark"><span class="dot"></span><span>The Hollin Perry Works</span></div>
  <h2 class="variety">Hollin<br>Traditional</h2>
  <p class="style-line">Dry Cyder</p>
  <div class="rule top"></div>
  <div class="facts">
    <div class="measures"><span class="vol">Alc vol:<br>6%</span><span>500ml</span></div>
    <p class="claim">Family craft cider makers using only premium apples from our own traditional Somerset orchard.</p>
    <div class="tree"><div class="tree-art" role="img" aria-label="Apple tree illustration"></div></div>
  </div>
  <div class="rule bottom"></div>
</section>

<section class="frame label back traditional col-back row-1">
  <div class="fruit-art" role="img" aria-label="Faint apple illustration"></div>
  <h2 class="variety">Hollin<br>Traditional</h2>
  <p class="company">The Hollin Perry Works Ltd.<br>42 Milford Terrace, Taunton, Somerset, TA4 9QJ</p>
  <div class="brand-mark"><span class="dot"></span><span>The Hollin Perry Works</span></div>
  <div class="rule top"></div>
  <div class="facts">
    <div class="measures"><span class="vol">Alc vol:<br>6%</span><span>500ml</span></div>
    <p class="claim">Family craft cider makers using only premium apples from our own traditional Somerset orchard.</p>
    <div class="tree"><div class="tree-art" role="img" aria-label="Apple tree illustration"></div><span class="batch">Batch number: 1701</span></div>
  </div>
  <div class="rule mid"></div>
  <p class="allergens">Allergens: contains sulphites for freshness</p>
  <div class="description">
    <p>A crisp and refreshing cider, its fresh apple aroma and slightly sweet, ripe apple flavors make it hard to resist.</p>
    <p>Developed to be the perfect balance of sweetness and dry acidity, it's a wonderful blended cider for the tenured cider geek or a freshman in the subject. It's a gluten free product made completely through the fermentation of apple juice and serves as a testament to the incredible fruit that comes right off the tree on farms across the country, hand selected by the cider makers.</p>
  </div>
  <div class="flourish" role="img" aria-label="Small gold flourish"></div>
</section>

<!-- Hollin Quarrow -->
<section class="frame label front quarrow col-front row-2">
  <div class="fruit-art" role="img" aria-label="Engraved apple and leaf illustration"></div>
  <div class="brand-mark"><span class="dot"></span><span>The Hollin Perry Works</span></div>
  <h2 class="variety">Hollin<br>Quarrow</h2>
  <p class="style-line">Single Variety Cyder</p>
  <div class="rule top"></div>
  <div class="facts">
    <div class="measures"><span class="vol">Alc vol:<br>6%</span><span>500ml</span></div>
    <p class="claim">Family craft cider makers using only premium apples from our own traditional Somerset orchard.</p>
    <div class="tree"><div class="tree-art" role="img" aria-label="Apple tree illustration"></div></div>
  </div>
  <div class="rule bottom"></div>
</section>

<section class="frame label back quarrow col-back row-2">
  <div class="fruit-art" role="img" aria-label="Faint apple illustration"></div>
  <h2 class="variety">Hollin<br>Quarrow</h2>
  <p class="company">The Hollin Perry Works Ltd.<br>42 Milford Terrace, Taunton, Somerset, TA4 9QJ</p>
  <div class="brand-mark"><span class="dot"></span><span>The Hollin Perry Works</span></div>
  <div class="rule top"></div>
  <div class="facts">
    <div class="measures"><span class="vol">Alc vol:<br>6%</span><span>500ml</span></div>
    <p class="claim">Family craft cider makers using only premium apples from our own traditional Somerset orchard.</p>
    <div class="tree"><div class="tree-art" role="img" aria-label="Apple tree illustration"></div><span class="batch">Batch number: 1701</span></div>
  </div>
  <div class="rule mid"></div>
  <p class="allergens">Allergens: contains sulphites for freshness</p>
  <div class="description">
    <p>A crisp and refreshing cider, its fresh apple aroma and slightly sweet, ripe apple flavors make it hard to resist.</p>
    <p>Developed to be the perfect balance of sweetness and dry acidity, it's a wonderful blended cider for the tenured cider geek or a freshman in the subject. It's a gluten free product made completely through the fermentation of apple juice and serves as a testament to the incredible fruit that comes right off the tree on farms across the country, hand selected by the cider makers.</p>
  </div>
  <div class="flourish" role="img" aria-label="Small gold flourish"></div>
</section>

<!-- Hollin Golden -->
<section class="frame label front golden col-front row-3">
  <div class="fruit-art" role="img" aria-label="Engraved apple and leaf illustration"></div>
  <div class="brand-mark"><span class="dot"></span><span>The Hollin Perry Works</span></div>
  <h2 class="variety">Hollin<br>Golden</h2>
  <p class="style-line">Medium Dry Cyder</p>
  <div class="rule top"></div>
  <div class="facts">
    <div class="measures"><span class="vol">Alc vol:<br>6%</span><span>500ml</span></div>
    <p class="claim">Family craft cider makers using only premium apples from our own traditional Somerset orchard.</p>
    <div class="tree"><div class="tree-art" role="img" aria-label="Apple tree illustration"></div></div>
  </div>
  <div class="rule bottom"></div>
</section>

<section class="frame label back golden col-back row-3">
  <div class="fruit-art" role="img" aria-label="Faint apple illustration"></div>
  <h2 class="variety">Hollin<br>Golden</h2>
  <p class="company">The Hollin Perry Works Ltd.<br>42 Milford Terrace, Taunton, Somerset, TA4 9QJ</p>
  <div class="brand-mark"><span class="dot"></span><span>The Hollin Perry Works</span></div>
  <div class="rule top"></div>
  <div class="facts">
    <div class="measures"><span class="vol">Alc vol:<br>6%</span><span>500ml</span></div>
    <p class="claim">Family craft cider makers using only premium apples from our own traditional Somerset orchard.</p>
    <div class="tree"><div class="tree-art" role="img" aria-label="Apple tree illustration"></div><span class="batch">Batch number: 1701</span></div>
  </div>
  <div class="rule mid"></div>
  <p class="allergens">Allergens: contains sulphites for freshness</p>
  <div class="description">
    <p>A crisp and refreshing cider, its fresh apple aroma and slightly sweet, ripe apple flavors make it hard to resist.</p>
    <p>Developed to be the perfect balance of sweetness and dry acidity, it's a wonderful blended cider for the tenured cider geek or a freshman in the subject. It's a gluten free product made completely through the fermentation of apple juice and serves as a testament to the incredible fruit that comes right off the tree on farms across the country, hand selected by the cider makers.</p>
  </div>
  <div class="flourish" role="img" aria-label="Small gold flourish"></div>
</section>

<p class="size-caption" style="left:83px">86mm x 93mm</p>
<p class="size-caption" style="left:387px">86mm x 93mm</p>

</body>
</html>
```